Business Card Design Project 4 Construction Business

I am after a creative, but sleek and simple/ clean business card design. This design will form the basis of future items and might include a logo or simply a creative way to lay out the text of my company name 'kestrel ventures'
I like the simplicity of black and white however I would also be happy to see a splash of colour introduced somehow to give the text some interest and make it stand out.
I would like a double sided card.
I am young (ish!) and professional, offering construction and project management services, what I don't want is the traditional builders type card featuring a cheesy hammer/ saw image etc.
As the company name, kestrel ventures, suggests, we focus on working closely and collaboratively together, in synergy with all stakeholders involved in the projects that we undertake
Construction

```html
<!DOCTYPE html>
<html lang="en">
<head>
<meta charset="utf-8">
<title>Kestrel Ventures – Business Card</title>
<link href="https://fonts.googleapis.com/css2?family=Cabin:ital,wght@0,400;0,600;1,400&display=swap" rel="stylesheet">
<style>
  :root {
    --backdrop: #333335;
    --paper: #ffffff;
    --ink: #111111;
    --grey: #6a6a6a;
    --sun: #ffcc0e;
    --amber: #f9a11b;
    --flame: #f06623;
    --band: #000000;
  }
  * { margin: 0; padding: 0; box-sizing: border-box; }
  html, body {
    width: 1200px; height: 1200px; overflow: hidden;
    background: var(--backdrop);
    font-family: "Cabin", "Trebuchet MS", sans-serif;
  }
  .card {
    position: absolute; top: 440px;
    width: 535px; height: 321px; overflow: hidden;
  }
  .card--front { left: 41px; background: var(--paper); }
  .card--back {
    left: 624px;
    background: linear-gradient(180deg, var(--sun) 0%, var(--amber) 40%, var(--flame) 82%);
  }
  .wordmark { position: absolute; color: var(--ink); font-weight: 600; text-transform: uppercase; line-height: 1; }
  .wordmark span { display: block; white-space: nowrap; }
  .card--front .wordmark { left: 53px; top: 55px; }
  .card--front .wordmark .main { font-size: 46px; letter-spacing: 10px; }
  .card--front .wordmark .sub { font-size: 25px; letter-spacing: 21px; margin-top: 12px; }
  .card--back .wordmark { left: 65px; top: 128px; }
  .card--back .wordmark .main { font-size: 32px; letter-spacing: 7px; }
  .card--back .wordmark .sub { font-size: 17px; letter-spacing: 14px; margin-top: 6px; }

  .role {
    position: absolute; right: 47px; top: 218px;
    font-style: italic; font-size: 22px; color: var(--grey);
  }
  .name-line {
    position: absolute; right: 40px; top: 240px;
    font-size: 36px; font-weight: 600; line-height: 1; letter-spacing: -0.5px;
  }
  .name-line::before {
    content: ""; position: absolute;
    right: 100%; margin-right: 3px; bottom: 0;
    width: 600px; height: 24px;
    border-bottom: 2.5px solid var(--sun);
    border-right: 2.5px solid var(--amber);
    border-bottom-right-radius: 10px;
  }
  .name-text {
    display: inline-block;
    background: linear-gradient(180deg, var(--sun), var(--flame));
    -webkit-background-clip: text; background-clip: text; color: transparent;
  }

  .contact {
    position: absolute; left: 289px; top: 93px;
    font-size: 14.5px; line-height: 17.7px; color: var(--ink); font-style: normal;
  }
  .contact .gap { height: 17.7px; }
  .band {
    position: absolute; left: 0; top: 265px; width: 100%; height: 56px;
    background: var(--band); border-top: 2px solid var(--paper);
  }
  .url {
    position: absolute; left: 56px; top: 8px;
    font-size: 15px; letter-spacing: 12.3px; color: var(--amber);
    text-transform: lowercase; white-space: nowrap;
  }
</style>
</head>
<body>
  <section class="card card--front">
    <div class="wordmark"><span class="main">Kestrel</span><span class="sub">Ventures</span></div>
    <div class="role">director</div>
    <div class="name-line"><span class="name-text">ALEX MARLOW</span></div>
  </section>

  <section class="card card--back">
    <div class="wordmark"><span class="main">Kestrel</span><span class="sub">Ventures</span></div>
    <address class="contact">
      <div>dummy&nbsp; dummy</div>
      <div>dummy dummy City, Country</div>
      <div class="gap"></div>
      <div>+63 917 5550142</div>
      <div>(083) 555 014</div>
      <div>(083) 555 0162</div>
      <div>alex@kestrelventures.com</div>
    </address>
    <div class="band"><div class="url">www.kestrelventures.com</div></div>
  </section>
</body>
</html>
```